Florida-based Coastal Landscaping Company Needs Letterhead Designs

We are a newly established Florida-based, coastal landscaping company that is looking for some really innovative flyers that we can use to get our name our to affluent consumers that live on the coast of Florida (think on the beach) and small to medium sized businesses in the same area. We will be handing out 100s of thousands of these, so need a great design

Target Market(s)

Affluent consumers and small to medium sized businesses

Industry/Entity Type

It Company

Font styles to use
Sans Serif

Colors

Designer to choose colors to be used in the design.

Requirements
Must have
• Need to have company name, logo, individual name, phone number and contact info
Nice to have
• Florida - looking, island looking / paradise, but needs to focus on the landscaping elements
Should not have
• Regular generic lawn company letterhead designs. We are a top tier landscape design / build plus maintenance firm, so not your mom and pop lawn mowing company

```html
<!DOCTYPE html>
<html lang="en">
<head>
<meta charset="utf-8">
<title>Tidegrove Letterhead</title>
<link href="https://fonts.googleapis.com/css2?family=Open+Sans:wght@400&display=swap" rel="stylesheet">
<style>
  :root {
    --backdrop: #07041c;
    --paper: #ffffff;
    --wave-blue: #0ba5d8;
    --ink: #231f20;
    --footer-text: #f2f2f2;
    --scene-fade: rgba(255, 255, 255, 0);
    --scene-aqua: #bfe6f1;
    --scene-sand: #e9eee8;
  }
  * { margin: 0; padding: 0; box-sizing: border-box; }
  html, body {
    width: 941px;
    height: 1200px;
    overflow: hidden;
    background: var(--backdrop);
  }
  .letterhead {
    position: absolute;
    left: 43px;
    top: 47px;
    width: 853px;
    height: 1104px;
    background: var(--paper);
    overflow: hidden;
    font-family: "Open Sans", Arial, sans-serif;
  }
  .header-wave {
    position: absolute;
    left: 0;
    top: 0;
    width: 853px;
    height: 200px;
  }
  .brand-name {
    position: absolute;
    right: 42px;
    top: 70px;
    font-size: 46px;
    font-weight: 400;
    letter-spacing: 9px;
    color: var(--ink);
    line-height: 1;
    background: var(--paper);
    padding-left: 12px;
  }
  .coastal-scene {
    position: absolute;
    left: 0;
    top: 640px;
    width: 853px;
    height: 464px;
    background: linear-gradient(
      to bottom,
      var(--scene-fade) 0%,
      var(--scene-aqua) 45%,
      var(--scene-sand) 100%
    );
  }
  .contact-bar {
    position: absolute;
    left: 0;
    top: 1054px;
    width: 853px;
    height: 37px;
    background: var(--ink);
    color: var(--footer-text);
    font-size: 15px;
    display: flex;
    align-items: center;
    justify-content: center;
    letter-spacing: 0.2px;
  }
</style>
</head>
<body>
  <main class="letterhead">
    <svg class="header-wave" viewBox="0 0 853 200" aria-hidden="true">
      <path fill="var(--wave-blue)"
        d="M0,84 C150,62 300,166 560,164 C690,162 785,135 853,108 L853,136 C785,165 690,186 560,184 C300,182 150,118 0,136 Z"/>
    </svg>
    <div class="brand-name">TIDEGROVE</div>

    <div class="coastal-scene" role="img"
      aria-label="Beach photograph area: parasol and two deck chairs on sand, sea and clouds, palm tree at right"></div>

    <footer class="contact-bar">555-013-2480 | hello@tidegrove.com | www.tidegrove.com</footer>
  </main>
</body>
</html>
```